I am looking for help designing my new business cards. I would like rounded edges and a raised logo on the back of the card. I have 2 Logos. One with a boat in it and one without. I'd like the one on the back to be the one that includes the boat and just the name on the front. I have included multiple formats of my logo. Please let me know if you need anymore.

Target Market(s)

Potential buyers and other sales brokers

Industry/Entity Type

Sales - Yacht / Boat Sales

Contact Information for Business Card

Id liike the front to include just the business name portion of the logo along with my name (Corwin Dalby), phone number (555.318.6027), website address (www.dalbymarineco.example) and not my physical address but just "Port Alden, SC". The back should include my full logo that has the boat included. This portion I'd prefer raised amd take up the majority of the space there. Thanks!!

Colors
0054AA
0677BA
7BADD7
CADEEF
E8F1F8
0094D4
00A9DD
6FCCEA
C7EBF8
E9F6FB

Requirements
Must have
• Double sided
Nice to have
• My email address: Corwin@dalbymarineco.example The NMTG logo somewhere small on the front of the card
Should not have
• My full address, prefer only "Port Alden, SC"

```html
<!DOCTYPE html>
<html lang="en">
<head>
<meta charset="utf-8">
<title>Dalby Marine Co. — Business Card</title>
<link rel="stylesheet" href="https://fonts.googleapis.com/css2?family=Montserrat:wght@400;500;700;800&display=swap">
<style>
  :root {
    --stage: #e9edf2;
    --navy: #0a3a80;
    --navy-deep: #052761;
    --sea: #0094d4;
    --sea-dark: #0677ba;
    --sky: #6fccea;
    --white: #ffffff;
    --divider: rgba(255,255,255,0.35);
  }
  * { box-sizing: border-box; margin: 0; padding: 0; }
  html, body { width: 1200px; height: 1200px; overflow: hidden; }
  body {
    background: var(--stage);
    font-family: "Montserrat", sans-serif;
    display: flex;
    flex-direction: column;
    align-items: center;
    justify-content: center;
    gap: 70px;
  }
  .card {
    position: relative;
    width: 700px;
    height: 400px;
    border-radius: 30px;
    overflow: hidden;
    box-shadow: 0 14px 34px rgba(5, 39, 97, 0.22);
  }
  .card-front { background: var(--white); }
  .front-wave { position: absolute; inset: 0; width: 100%; height: 100%; }

  .brand-name {
    position: absolute;
    left: 70px;
    top: 100px;
    width: 440px;
    text-align: center;
    font-weight: 800;
    font-size: 36px;
    letter-spacing: 2px;
    color: var(--navy);
    line-height: 1;
    white-space: nowrap;
  }

  .holder {
    position: absolute;
    left: 48px;
    bottom: 56px;
  }
  .holder-name {
    font-weight: 700;
    font-size: 26px;
    letter-spacing: 1px;
    color: var(--sea);
    text-transform: uppercase;
  }
  .holder-company {
    font-weight: 500;
    font-size: 15px;
    letter-spacing: 1px;
    color: var(--white);
    text-transform: uppercase;
    margin-top: 4px;
  }
  .front-divider {
    position: absolute;
    left: 362px;
    top: 232px;
    width: 1px;
    height: 130px;
    background: var(--divider);
  }
  .contact-list {
    position: absolute;
    left: 390px;
    top: 196px;
    list-style: none;
    color: var(--white);
    font-size: 15px;
    font-weight: 400;
  }
  .contact-list li {
    display: flex;
    align-items: center;
    gap: 10px;
    margin-bottom: 11px;
    white-space: nowrap;
  }
  .contact-list svg { width: 17px; height: 17px; flex: none; }

  .card-back {
    background: radial-gradient(ellipse at 35% 30%, var(--navy) 0%, var(--navy-deep) 100%);
    display: flex;
    align-items: center;
    justify-content: center;
  }
  .back-brand {
    font-weight: 800;
    font-size: 52px;
    letter-spacing: 3px;
    color: var(--white);
    white-space: nowrap;
  }
</style>
</head>
<body>

<section class="card card-front" aria-label="Card front">
  <svg class="front-wave" viewBox="0 0 700 400" preserveAspectRatio="none" aria-hidden="true">
    <path d="M0 222 Q380 230 700 52 L700 400 L0 400 Z" fill="var(--sea-dark)"/>
    <path d="M0 232 Q380 240 700 62 L700 400 L0 400 Z" fill="var(--navy)"/>
  </svg>

  <div class="brand-name">DALBY MARINE CO.</div>

  <div class="holder">
    <div class="holder-name">Corwin Dalby</div>
    <div class="holder-company">Dalby Marine Co.</div>
  </div>

  <div class="front-divider"></div>

  <ul class="contact-list">
    <li>
      <svg viewBox="0 0 24 24"><path fill="var(--sea)" d="M6.6 10.8a15 15 0 006.6 6.6l2.2-2.2c.3-.3.7-.4 1-.2 1.1.4 2.3.6 3.6.6.6 0 1 .4 1 1V20c0 .6-.4 1-1 1A17 17 0 013 4c0-.6.4-1 1-1h3.5c.6 0 1 .4 1 1 0 1.3.2 2.5.6 3.6.1.3 0 .7-.2 1z"/></svg>
      (555) 318-6027
    </li>
    <li>
      <svg viewBox="0 0 24 24"><rect x="2" y="5" width="20" height="14" rx="1.5" fill="none" stroke="var(--sea)" stroke-width="2"/><path d="M2.5 6l9.5 7 9.5-7" fill="none" stroke="var(--sea)" stroke-width="2"/></svg>
      corwin@dalbymarineco.example
    </li>
    <li>
      <svg viewBox="0 0 24 24" fill="none" stroke="var(--sea)" stroke-width="1.8"><circle cx="12" cy="12" r="9.5"/><ellipse cx="12" cy="12" rx="4" ry="9.5"/><path d="M2.5 12h19M4 7h16M4 17h16"/></svg>
      www.dalbymarineco.example
    </li>
    <li>
      <svg viewBox="0 0 24 24"><path fill="none" stroke="var(--sea)" stroke-width="2" d="M12 22s7-7.2 7-12.5A7 7 0 005 9.5C5 14.8 12 22 12 22z"/><circle cx="12" cy="9.5" r="2.5" fill="var(--sea)"/></svg>
      Port Alden, SC
    </li>
  </ul>
</section>

<section class="card card-back" aria-label="Card back">
  <div class="back-brand">DALBY MARINE CO.</div>
</section>

</body>
</html>
```